Capacity building in Resource Management

Need design of a business card (later to be completed by letterhead and webdesign in same fashion) for a professional who works in the field of capacity building of professionals in mostly developing countries in the field waste/resource management, waste prevention/reduction, cleaner production, stakeholders involvement, etc.
Info on business cards is to include provided logo, info in provided file and picture.

Industry/Entity Type

Business

Contact Information for Business Card

White background

Font styles to use
Sans Serif

Colors

Designer to choose colors to be used in the design.

```html
<!DOCTYPE html>
<html lang="en">
<head>
<meta charset="utf-8">
<title>Business Card – Jonas Verbeek</title>
<link href="https://fonts.googleapis.com/css2?family=Open+Sans:wght@400;600;800&display=swap" rel="stylesheet">
<style>
  :root {
    --green: #4f7f2e;
    --green-dark: #3d6623;
    --ink: #2b2b2b;
    --rule: #b9b9a8;
    --paper: #ffffff;
    --backdrop: #e7e9e6;
    --photo-a: #8a9a6c;
    --photo-b: #c9c4b6;
  }
  * { margin: 0; padding: 0; box-sizing: border-box; }
  html, body {
    width: 1200px; height: 619px; overflow: hidden;
    background: var(--backdrop);
    font-family: "Open Sans", Arial, sans-serif;
  }
  .card {
    position: absolute; left: 70px; top: 12px;
    width: 1060px; height: 595px;
    background: var(--paper);
    box-shadow: 0 4px 18px rgba(0,0,0,.12);
    overflow: hidden;
  }
  .brand {
    position: absolute; left: 170px; top: 176px;
    display: flex; align-items: center; gap: 14px;
  }
  .brand-mark {
    width: 34px; height: 34px; border-radius: 50%;
    background: var(--green); flex: none;
  }
  .brand-name {
    font-weight: 800; font-size: 44px;
    color: var(--green); line-height: 1; white-space: nowrap;
  }
  .portrait {
    position: absolute; left: 700px; top: 130px;
    width: 270px; height: 200px; border-radius: 50%;
    background: radial-gradient(ellipse at 55% 40%, var(--photo-b), var(--photo-a));
    box-shadow: 0 2px 8px rgba(0,0,0,.25);
  }
  .social {
    position: absolute; left: 0; top: 290px;
    list-style: none;
  }
  .social li {
    display: flex; align-items: center; gap: 14px;
    height: 44px; margin-bottom: 7px; padding-left: 26px;
    background: var(--green); color: #fff;
    border-radius: 0 22px 22px 0;
    font-size: 17px; font-weight: 400; white-space: nowrap;
  }
  .social li:nth-child(1) { width: 262px; }
  .social li:nth-child(2) { width: 246px; }
  .social li:nth-child(3) { width: 232px; }
  .social li:nth-child(4) { width: 220px; }
  .social .mark {
    width: 18px; height: 18px; border-radius: 50%; background: #fff; flex: none;
  }
  .contact {
    position: absolute; left: 660px; top: 390px; width: 370px;
  }
  .contact-name {
    font-size: 30px; font-weight: 800; color: var(--green-dark);
    padding-bottom: 6px; border-bottom: 2px solid var(--rule);
    margin-bottom: 12px;
  }
  .contact-list { list-style: none; }
  .contact-list li {
    display: flex; align-items: center; gap: 12px;
    font-size: 15px; color: var(--ink); height: 27px; white-space: nowrap;
  }
  .contact-list svg { width: 16px; height: 16px; flex: none; fill: var(--green); }
</style>
</head>
<body>
  <main class="card">
    <div class="brand">
      <span class="brand-mark"></span>
      <span class="brand-name">Oakridge Training</span>
    </div>

    <div class="portrait" role="img" aria-label="Portrait photo of Jonas Verbeek outdoors"></div>

    <ul class="social">
      <li><span class="mark"></span>@jonasverbeek</li>
      <li><span class="mark"></span>verbeek1987</li>
      <li><span class="mark"></span>Jonas Verbeek</li>
      <li><span class="mark"></span>+49 1500 123 4567</li>
    </ul>

    <section class="contact">
      <h1 class="contact-name">Jonas Verbeek</h1>
      <ul class="contact-list">
        <li>
          <svg viewBox="0 0 16 16" aria-hidden="true"><path d="M8 0a5.5 5.5 0 0 0-5.5 5.5C2.5 10 8 16 8 16s5.5-6 5.5-10.5A5.5 5.5 0 0 0 8 0zm0 8a2.5 2.5 0 1 1 0-5 2.5 2.5 0 0 1 0 5z"/></svg>
          Lindenweg 12 10117 Berlin Germany
        </li>
        <li>
          <svg viewBox="0 0 16 16" aria-hidden="true"><path d="M0 3h16v1.2L8 9 0 4.2z"/><path d="M0 5.8l8 4.8 8-4.8V13H0z"/></svg>
          jonas.verbeek@oakridgetraining.com
        </li>
        <li>
          <svg viewBox="0 0 16 16" aria-hidden="true"><circle cx="8" cy="8" r="7" fill="none" stroke="currentColor"/><path d="M8 0a8 8 0 1 0 0 16A8 8 0 0 0 8 0zm0 1.5c.9 0 2 1.9 2.3 5.2H5.7C6 3.4 7.1 1.5 8 1.5zM1.6 7.3h2.6c0 .5 0 1 .1 1.4H1.6a6 6 0 0 1 0-1.4zm0 2.8h2.8c.2 1.7.7 3.1 1.3 4A6.5 6.5 0 0 1 1.6 10.1zM8 14.5c-.9 0-2-1.9-2.3-4.4h4.6C10 12.6 8.9 14.5 8 14.5zm2.3-5.8H5.7a13 13 0 0 1 0-1.4h4.6a13 13 0 0 1 0 1.4zm0 5.4c.6-.9 1.1-2.3 1.3-4h2.8a6.5 6.5 0 0 1-4.1 4zm1.4-5.4c.1-.4.1-.9.1-1.4h2.6a6 6 0 0 1 0 1.4z"/></svg>
          www.oakridgetraining.com
        </li>
        <li>
          <svg viewBox="0 0 16 16" aria-hidden="true"><path d="M3.6.6 6 3.3c.4.4.4 1 0 1.4L4.8 6a10 10 0 0 0 5.2 5.2l1.3-1.2c.4-.4 1-.4 1.4 0l2.7 2.4c.4.4.4 1 0 1.4l-1.3 1.4c-.6.6-1.5.8-2.3.5A15 15 0 0 1 .3 4.3c-.3-.8-.1-1.7.5-2.3L2.2.6c.4-.4 1-.4 1.4 0z"/></svg>
          +49 1500 123 4567
        </li>
      </ul>
    </section>
  </main>
</body>
</html>
```